Fleur Vallon Riding School Flyer Design

We need a flyer for our Horse riding school, called Fleur Vallon Riding School.

At Fleur Vallon Riding School, Horses and ponies are carefully matched to suit each rider's experience, ability and confidence. I am a Qualified instructor, equipped to train all levels from nervous beginners to the more advanced.

Horse riding is fun! Riders, particularly children, are taught not only skills on the horse, but skills that are integral to good horsemanship and ownership of horses.

We regularly host Ladies Days, Guest Instructors, 1 hour Trail Rides and Pony Ride Days!

We teach people how to interact safely with, and care for horses so they develop a genuine love and respect for the animals and the sport.

In addition to fundamental riding techniques including walk, trot, and canter, we teach our students:
Grooming and Care of horses, Safety around horses, Balance and Co-Ordination, How to saddle up and care for Tack, Responsibility for equipment and horse, Confidence and Confidence Building for all Ages.

Private and group lessons start at 5 years of age upwards.

We recommend children 4 years and under partake in 15 minute pony rides, mainly due to their attention span!

```html
<!DOCTYPE html>
<html lang="en">
<head>
<meta charset="utf-8">
<title>Fleur Vallon Riding School</title>
<link rel="stylesheet" href="https://fonts.googleapis.com/css2?family=Arimo:wght@400;700&family=Cormorant+Upright:wght@500&display=swap">
<style>
  :root {
    --bg-deep: #0d0807;
    --bg-warm: #2a1713;
    --gold: #efd68c;
    --white: #ffffff;
    --lavender: #c9c2ea;
    --silver: #c8c8cc;
    --silver-dark: #6c6c72;
    --photo-chestnut-a: #b3673a;
    --photo-chestnut-b: #6e3b22;
    --photo-grey-a: #9a9a9a;
    --photo-grey-b: #3a3a3a;
  }
  * { margin: 0; padding: 0; box-sizing: border-box; }
  html, body { width: 1200px; height: 850px; overflow: hidden; background: var(--bg-deep); }
  .flyer {
    position: relative;
    width: 1200px; height: 850px; overflow: hidden;
    background:
      radial-gradient(ellipse at 40% 35%, var(--bg-warm) 0%, rgba(42,23,19,0.6) 40%, var(--bg-deep) 80%);
    font-family: "Arimo", Arial, sans-serif;
    color: var(--white);
  }
  .brand {
    position: absolute; left: 60px; top: 22px; width: 460px;
    text-align: center; color: var(--white); font-family: "Arimo", Arial, sans-serif; font-weight: 400;
    white-space: nowrap;
  }
  .brand-dot {
    width: 160px; height: 160px; margin: 0 auto 60px;
    border: 2px solid var(--white); border-radius: 50%;
  }
  .brand-name { font-size: 40px; letter-spacing: 7px; line-height: 44px; }
  .brand-sub { font-size: 22px; letter-spacing: 5px; line-height: 26px; margin-top: 14px; }
  .photo {
    position: absolute; top: -4px; height: 338px;
    border: 4px solid var(--silver);
    box-shadow: 0 0 0 1px var(--silver-dark);
  }
  .photo-chestnut { left: 697px; width: 234px;
    background: linear-gradient(160deg, var(--photo-chestnut-a), var(--photo-chestnut-b)); }
  .photo-grey { left: 970px; width: 236px;
    background: linear-gradient(160deg, var(--photo-grey-a), var(--photo-grey-b)); }
  .intro {
    position: absolute; left: 33px; top: 358px; width: 1150px;
    font-family: "Cormorant Upright", Georgia, serif; font-weight: 500;
    font-size: 28px; line-height: 29px; letter-spacing: 0.9px; color: var(--gold);
    white-space: nowrap;
  }
  .body-copy { position: absolute; left: 30px; top: 460px; width: 1170px; font-size: 16px; }
  .body-copy p { margin-bottom: 33px; line-height: 20px; }
  .body-copy .lead { font-size: 18px; margin-bottom: 3px; line-height: 22px; }
  .skills { font-size: 14.5px; line-height: 26px; white-space: nowrap; }
  .recommend {
    position: absolute; left: 30px; top: 752px; color: var(--lavender); white-space: nowrap;
  }
  .recommend-head { font-size: 47px; line-height: 46px; }
  .recommend-sub { font-size: 20px; line-height: 22px; }
  .age-badge { position: absolute; left: 930px; top: 590px; width: 260px; height: 260px; }
</style>
</head>
<body>
<main class="flyer">
  <header class="brand">
    <div class="brand-dot"></div>
    <div class="brand-name">FLEUR VALLON</div>
    <div class="brand-sub">RIDING SCHOOL</div>
  </header>

  <div class="photo photo-chestnut" role="img" aria-label="Photo of a chestnut horse with a white blaze wearing a halter"></div>
  <div class="photo photo-grey" role="img" aria-label="Black and white photo of a dark horse standing by a paddock fence"></div>

  <p class="intro">At Fleur Vallon Riding School, Horses and ponies are carefully matched to suit each rider's<br>experience, ability and confidence. I am a Qualified instructor, equipped to train all levels from<br>nervous beginners to the more advanced.</p>

  <section class="body-copy">
    <p>Horse riding is fun! Riders, particularly children, are taught not only skills on the horse, but skills that are integral to good horsemanship and ownership of horses.</p>
    <p>We regularly host Ladies Days, Guest Instructors, 1 hour Trail Rides and Pony Ride Days!</p>
    <p>We teach people how to interact safely with, and care for horses so they develop a genuine love and respect for the animals and the sport.</p>
    <p class="lead">In addition to fundamental riding techniques including walk, trot, and canter, we teach our students:</p>
    <p class="skills">Grooming and Care of horses, Safety around horses, Balance and Co-Ordination, How to saddle up and care for Tack,<br>Responsibility for equipment and horse, Confidence and Confidence Building for all Ages.</p>
  </section>

  <div class="recommend">
    <div class="recommend-head">We recommend children 4 years</div>
    <div class="recommend-sub">and under partake in 15 minute pony rides, mainly due to their attention span!</div>
  </div>

  <svg class="age-badge" viewBox="0 0 260 260" aria-label="Private and group lessons start at 5 years of age upwards">
    <defs>
      <radialGradient id="badgeFill" cx="50%" cy="45%" r="55%">
        <stop offset="0%" stop-color="#1a1a1c"/>
        <stop offset="100%" stop-color="#050505"/>
      </radialGradient>
      <linearGradient id="badgeRing" x1="0" y1="0" x2="1" y2="1">
        <stop offset="0%" stop-color="#f2f2f4"/>
        <stop offset="50%" stop-color="#7a7a80"/>
        <stop offset="100%" stop-color="#e0e0e4"/>
      </linearGradient>
      <path id="arcTop" d="M 30 130 A 100 100 0 0 1 230 130"/>
      <path id="arcBottom" d="M 40 130 A 90 90 0 0 0 220 130"/>
    </defs>
    <circle cx="130" cy="130" r="124" fill="url(#badgeFill)" stroke="url(#badgeRing)" stroke-width="8"/>
    <circle cx="130" cy="130" r="82" fill="none" stroke="#5a5a60" stroke-width="1.5"/>
    <text font-family="Arimo, Arial, sans-serif" font-size="17" fill="#ffffff">
      <textPath href="#arcTop" startOffset="50%" text-anchor="middle">Private and group lessons start</textPath>
    </text>
    <text font-family="Arimo, Arial, sans-serif" font-size="26" fill="#ffffff" letter-spacing="1">
      <textPath href="#arcBottom" startOffset="50%" text-anchor="middle" dominant-baseline="hanging">Upwards</textPath>
    </text>
    <rect x="58" y="78" width="144" height="104" rx="12" fill="#0c0c0d" stroke="url(#badgeRing)" stroke-width="2"/>
    <g font-family="Arimo, Arial, sans-serif" font-size="24" fill="#ffffff" text-anchor="middle">
      <text x="130" y="107">AT</text>
      <text x="130" y="138">5 YEARS</text>
      <text x="130" y="169">OF AGE</text>
    </g>
  </svg>
</main>
</body>
</html>
```